Bright Orbit IT company Soho london Stationary

We've just had a new logo designed on Pixel Harbor and we now need some Stationary to go with it.
We're a small IT support firm supporting Design companies in Soho London. Most of our clients work on Zorvas and a relatively creative so we want a relatively informal design on our stationary to reflect this.
We'd like to stick with the green in the logo but we're not adverse to adding another few colours to the palette.
Please see the attached file for our logo and not our website.

It Company

```html
<!DOCTYPE html>
<html lang="en">
<head>
<meta charset="utf-8">
<title>Bright Orbit – Stationery</title>
<link rel="stylesheet" href="https://fonts.googleapis.com/css2?family=Didact+Gothic&display=swap">
<style>
  :root{
    --green:#b5e61d;
    --black:#050505;
    --ink:#111111;
    --paper:#ffffff;
    --backdrop:#6e6e6e;
    --rule:#222222;
  }
  *{box-sizing:border-box;margin:0;padding:0}
  html,body{width:862px;height:1200px;overflow:hidden;background:var(--backdrop)}
  body{font-family:"Didact Gothic",Arial,sans-serif;color:var(--ink);position:relative}
  .sheet{position:absolute;left:18px;top:18px;width:792px;height:1120px;background:var(--paper)}
  .brand{display:flex;align-items:center;gap:10px;color:var(--green);font-family:"Didact Gothic",Arial,sans-serif;font-weight:400;white-space:nowrap}
  .brand__dot{display:inline-block;border-radius:50%;background:var(--green)}
  .sheet__brand{position:absolute;right:70px;top:48px;font-size:40px}
  .sheet__brand .brand__dot{width:26px;height:26px}
  .card{position:absolute;width:330px;height:190px;overflow:hidden}
  .card--back{left:82px;top:150px;background:var(--black);color:#fff}
  .card--front{left:440px;top:150px;background:var(--paper);border:1px solid #ccc}
  .card__person{position:absolute;left:16px;top:18px;font-size:13px;font-style:italic;line-height:20px}
  .card__address{position:absolute;right:14px;top:30px;font-size:10px;line-height:13px;text-align:right}
  .card__contact{position:absolute;left:12px;top:100px;font-size:12px;line-height:17px}
  .card__mark{position:absolute;right:20px;bottom:16px;width:60px;height:60px;border-radius:50%;background:var(--green)}
  .card__brand{position:absolute;left:70px;top:42px;font-size:32px}
  .card__brand .brand__dot{width:20px;height:20px}
  .card__band{position:absolute;left:0;right:0;bottom:18px;height:48px;background:var(--black);color:#fff;font-size:10px;line-height:13px;text-align:right;padding:20px 16px 0}
  .envelope{position:absolute;left:70px;top:380px;width:680px;height:330px;background:var(--paper);border:1px solid #ccc}
  .envelope__brand{position:absolute;right:40px;top:40px;font-size:30px}
  .envelope__brand .brand__dot{width:18px;height:18px}
  .envelope__mark{position:absolute;left:30px;top:140px;width:56px;height:56px;border-radius:50%;background:var(--green)}
  .envelope__sender{position:absolute;left:30px;top:212px;font-size:11px;line-height:14px}
  .envelope__sender p+p{margin-top:10px}
  .envelope__line{position:absolute;left:390px;width:230px;border-top:1px solid var(--rule)}
  .sheet__mark{position:absolute;left:46px;top:810px;width:110px;height:110px;border-radius:50%;background:var(--green)}
  .sheet__footer{position:absolute;left:44px;top:944px;font-size:15px;line-height:20px}
  .sheet__footer p+p{margin-top:20px}
</style>
</head>
<body>
<main class="sheet">
  <div class="brand sheet__brand"><span class="brand__dot"></span>Bright Orbit</div>

  <section class="card card--back">
    <div class="card__person">Name<br>Designation</div>
    <div class="card__address">Bright Orbit Ltd.<br>22 Kestrel Lane<br>London<br>W1X 9QT</div>
    <div class="card__contact">Mob 0000000000<br>Email name@mailbox.it</div>
    <div class="card__mark"></div>
  </section>

  <section class="card card--front">
    <div class="brand card__brand"><span class="brand__dot"></span>Bright Orbit</div>
    <div class="card__band">Web:www.bright-orbit.it<br>email: info@bright-orbit.it</div>
  </section>

  <section class="envelope">
    <div class="brand envelope__brand"><span class="brand__dot"></span>Bright Orbit</div>
    <div class="envelope__mark"></div>
    <div class="envelope__sender">
      <p>Bright Orbit Ltd.<br>22 Kestrel Lane<br>London<br>W1X 9QT</p>
      <p>Phone: 0203 555 0148<br>Web: http://bright-orbit.it<br>email: info@bright-orbit.it</p>
    </div>
    <div class="envelope__line" style="top:176px"></div>
    <div class="envelope__line" style="top:210px"></div>
  </section>

  <div class="sheet__mark"></div>
  <footer class="sheet__footer">
    <p>Bright Orbit Ltd.<br>22 Kestrel Lane<br>London<br>W1X 9QT</p>
    <p>Phone: 0203 555 0148<br>Web: http://bright-orbit.it<br>email: info@bright-orbit.it</p>
  </footer>
</main>
</body>
</html>
```